dirty dancer in bathtub promotion

Need graphics for side of bathtub for a party -event promotion ( as shown in photo below). graphics must be contained in an area of 38” x 15” for entire name.
Company name that will be written across the tub is
MERIDIAN TILEWORK COLLECTIVE The theme event is Art Deco so font should be in an Art Deco like font and SEXY

Target Market(s)

Architects and designers

Font styles to use
Other font styles liked:
• Art Deco

Colors
ffffff
edf7f6

Requirements
Must have
• Professional - creative white lettering
Nice to have
• Art Deco font MUST BE ALL WHITE...(as bathtub is dark copper color )

```html
<!DOCTYPE html>
<html lang="en">
<head>
<meta charset="utf-8">
<title>Meridian Tilework Collective – Tub Banner</title>
<link rel="stylesheet" href="https://fonts.googleapis.com/css2?family=Federo&display=swap">
<style>
  :root {
    --copper-deep: #5a1c10;
    --copper: #7a2a17;
    --copper-warm: #8a3019;
    --lettering: #ffffff;
  }
  html, body {
    margin: 0;
    padding: 0;
    overflow: hidden;
  }
  body {
    width: 1200px;
    height: 475px;
  }
  .tub-panel {
    position: relative;
    width: 1200px;
    height: 475px;
    overflow: hidden;
    background:
      radial-gradient(ellipse 420px 180px at 200px 90px, rgba(138,48,25,0.45), transparent 70%),
      radial-gradient(ellipse 380px 160px at 900px 400px, rgba(138,48,25,0.4), transparent 70%),
      radial-gradient(ellipse 300px 200px at 1150px 120px, rgba(70,20,10,0.45), transparent 70%),
      radial-gradient(ellipse 260px 140px at 60px 330px, rgba(70,20,10,0.4), transparent 70%),
      linear-gradient(135deg, var(--copper) 0%, var(--copper-warm) 45%, var(--copper) 70%, var(--copper-deep) 100%);
  }
  .name-lockup {
    position: absolute;
    left: 0;
    top: 0;
    display: block;
    width: 1200px;
    height: 475px;
  }
  .company-name {
    font-family: "Federo", "Poiret One", sans-serif;
    font-size: 74px;
    font-weight: 400;
    fill: var(--lettering);
  }
</style>
</head>
<body>
  <main class="tub-panel">
    <svg class="name-lockup" viewBox="0 0 1200 475" aria-label="Meridian Tilework Collective">
      <text class="company-name" x="70" y="264" textLength="1062" lengthAdjust="spacing">MERIDIAN TILEWORK COLLECTIVE</text>
    </svg>
  </main>
</body>
</html>
```